Australian IT Company New Logo Business Cards Required

We are a computer consultancy / MSP located in Brisbane Australia looking to have business cards designed with our new logo, we are looking for something professional that catches the eye.
I can provide the logo in other formats if required, let's see what you can create!

```html
<!DOCTYPE html>
<html lang="en">
<head>
<meta charset="utf-8">
<title>Verdaro Business Cards</title>
<link rel="stylesheet" href="https://fonts.googleapis.com/css2?family=Source+Sans+3:wght@400;600;700&display=swap">
<style>
  :root {
    --page: #e3e3e3;
    --charcoal: #2c2b29;
    --paper: #f4f4f4;
    --green: #83bd41;
    --grey-text: #7b7b7b;
    --ink: #2a2a2a;
    --white: #ffffff;
  }
  html, body {
    margin: 0;
    width: 1200px;
    height: 960px;
    overflow: hidden;
    background: var(--page);
    font-family: "Source Sans 3", sans-serif;
  }
  .canvas { position: relative; width: 1200px; height: 960px; }
  .card {
    position: absolute;
    left: 311px;
    width: 578px;
    height: 354px;
    overflow: hidden;
  }
  .card-front { top: 106px; background: var(--charcoal); }
  .card-back { top: 505px; background: var(--paper); }

  .front-lockup {
    position: absolute;
    top: 148px;
    left: 0; right: 0;
    text-align: center;
  }
  .brand-name {
    margin: 0;
    color: var(--green);
    font-weight: 700;
    letter-spacing: 1px;
    line-height: 1;
  }
  .front-lockup .brand-name { font-size: 56px; }
  .front-lockup .tagline {
    margin: 6px 0 0;
    color: var(--white);
    font-size: 17px;
    font-weight: 700;
    letter-spacing: 1.2px;
  }
  .front-web {
    position: absolute;
    top: 305px;
    left: 0; right: 0;
    text-align: center;
    color: var(--white);
    font-size: 15px;
    letter-spacing: 1px;
  }
  .front-web .accent { color: var(--green); }

  .back-lockup { position: absolute; left: 40px; top: 62px; }
  .back-lockup .brand-name { font-size: 40px; }
  .back-lockup .tagline {
    margin: 4px 0 0;
    color: var(--grey-text);
    font-size: 13px;
    font-weight: 700;
    letter-spacing: 1px;
  }
  .brand-field { position: absolute; left: 0; top: 0; }

  .contact {
    position: absolute;
    right: 39px;
    top: 175px;
    text-align: right;
    color: var(--ink);
    font-size: 14.5px;
  }
  .contact-name {
    margin: 0;
    color: var(--white);
    font-size: 18px;
    font-weight: 700;
  }
  .contact-role { margin: 2px 0 0; font-size: 14.5px; }
  .contact-list { list-style: none; margin: 22px 0 0; padding: 0; }
  .contact-list li {
    display: flex;
    justify-content: flex-end;
    align-items: center;
    gap: 4px;
    height: 19.5px;
  }
  .contact-list svg { width: 13px; height: 13px; }
  .contact-address { margin: 16px 0 0; }
</style>
</head>
<body>
<main class="canvas">
  <section class="card card-front" aria-label="Card front">
    <div class="front-lockup">
      <p class="brand-name">VERDARO</p>
      <p class="tagline">IT SOLUTIONS FOR SMALL BUSINESS</p>
    </div>
    <p class="front-web">www.<span class="accent">verdaro</span>.com</p>
  </section>

  <section class="card card-back" aria-label="Card back">
    <svg class="brand-field" width="578" height="354" viewBox="0 0 578 354" role="img" aria-label="Large green brand decoration">
      <circle cx="400" cy="360" r="310" fill="var(--green)"/>
    </svg>
    <div class="back-lockup">
      <p class="brand-name">VERDARO</p>
      <p class="tagline">IT SOLUTIONS FOR SMALL BUSINESS</p>
    </div>
    <div class="contact">
      <p class="contact-name">Daniel Hartley</p>
      <p class="contact-role">Founder</p>
      <ul class="contact-list">
        <li>07 3000 4127
          <svg viewBox="0 0 24 24" aria-hidden="true"><path fill="#fff" d="M6.6 10.8a15.2 15.2 0 0 0 6.6 6.6l2.2-2.2c.3-.3.7-.4 1-.2 1.1.4 2.3.6 3.6.6.6 0 1 .4 1 1V20c0 .6-.4 1-1 1A17 17 0 0 1 3 4c0-.6.4-1 1-1h3.5c.6 0 1 .4 1 1 0 1.3.2 2.5.6 3.6.1.3 0 .7-.2 1z"/></svg>
        </li>
        <li>support@verdaro.com
          <svg viewBox="0 0 24 24" aria-hidden="true"><rect x="2" y="5" width="20" height="14" fill="none" stroke="#fff" stroke-width="2"/><path d="M2 5l10 8 10-8" fill="none" stroke="#fff" stroke-width="2"/></svg>
        </li>
        <li>www.verdaro.com
          <svg viewBox="0 0 24 24" aria-hidden="true"><g fill="none" stroke="#fff" stroke-width="1.8"><circle cx="12" cy="12" r="10"/><ellipse cx="12" cy="12" rx="4.5" ry="10"/><path d="M2 12h20M4 7h16M4 17h16"/></g></svg>
        </li>
      </ul>
      <p class="contact-address">Ash Lane, Redfield, QLD 4000</p>
    </div>
  </section>
</main>
</body>
</html>
```